Ad design for a macarons brand

We are a dessert brand with one product line: macarons. Our products delight. Every bite is a dream!

We are launching a new product and would like to lunch a small tactical campaign for the product to boost sales.

The new macron is mango ganache and the middle a mix of sour mango and yuzu (https://www.plumvarell.com/about-the-fruit-584302).

Here are some images we took of the new macaron
https://www.fennlocker.com/sh/qrtwpzhkvbmls/AAFJtRWD-nxPlkhQZ7CeW4DLp?dl=0

I attach the brand guideline document.

Required sizes

1080 x 1350
1080 x 1920

```html
<!DOCTYPE html>
<html lang="en">
<head>
<meta charset="utf-8">
<title>Dorelle – Mango &amp; Yuzu</title>
<link href="https://fonts.googleapis.com/css2?family=Montserrat:wght@500&display=swap" rel="stylesheet">
<style>
  :root {
    --backdrop: #eceeef;
    --poster-orange: #d8933a;
    --brand-maroon: #4e1619;
    --flavour-green: #66713f;
    --cream: #f6ead0;
    --heart-rust: #a84e2c;
    --photo-light: #f3ead8;
    --photo-gold: #e3a93c;
    --photo-amber: #c9822c;
  }
  * { margin: 0; padding: 0; box-sizing: border-box; }
  html, body {
    width: 1200px;
    height: 899px;
    overflow: hidden;
    background: var(--backdrop);
    font-family: "Montserrat", sans-serif;
  }
  .poster {
    position: absolute;
    left: 328px;
    top: 110px;
    width: 543px;
    height: 680px;
    background: var(--poster-orange);
  }
  .brand-badge {
    position: absolute;
    left: 153px;
    top: 43px;
    width: 236px;
    height: 236px;
    border-radius: 50%;
    background: var(--brand-maroon);
    display: flex;
    align-items: center;
    justify-content: center;
  }
  .brand-name {
    color: var(--cream);
    font-weight: 500;
    font-size: 34px;
    letter-spacing: 3px;
  }
  .flavour-band {
    position: absolute;
    left: 124px;
    top: 304px;
    width: 296px;
    height: 39px;
    background: var(--flavour-green);
    color: var(--cream);
    font-weight: 500;
    font-size: 22px;
    letter-spacing: 5px;
    display: flex;
    align-items: center;
    justify-content: center;
  }
  .product-heart {
    position: absolute;
    left: 122px;
    top: 359px;
    width: 302px;
    height: 272px;
  }
</style>
</head>
<body>
  <main class="poster">
    <div class="brand-badge">
      <span class="brand-name">DORELLE</span>
    </div>
    <div class="flavour-band">MANGO &amp; YUZU</div>
    <svg class="product-heart" viewBox="-1 -1 302 272" role="img" aria-label="Photo of mango and yuzu macarons piled on white parchment with fresh mango behind">
      <defs>
        <linearGradient id="macaronPhoto" x1="0" y1="0" x2="0.6" y2="1">
          <stop offset="0" stop-color="var(--photo-light)"/>
          <stop offset="0.35" stop-color="var(--photo-gold)"/>
          <stop offset="0.75" stop-color="var(--photo-amber)"/>
          <stop offset="1" stop-color="var(--photo-light)"/>
        </linearGradient>
      </defs>
      <path d="M150 48 C130 8 70 -4 32 18 C-6 42 -2 110 40 158 L150 266 L260 158 C302 110 306 42 268 18 C230 -4 170 8 150 48 Z"
            fill="url(#macaronPhoto)" stroke="var(--heart-rust)" stroke-width="3"/>
    </svg>
  </main>
</body>
</html>
```